Harrowgate Properties Needs New Stationery Design

We need new clean and white stationery for our property management company based in Winnipeg, Manitoba, Canada. We manage condominium and commercial properties. Additionally, we do real estate development and commercial leasing.

We'll require the following:
- Business cards
- Letterhead*
- Envelope (we mainly use #10, single window envelope)
- Fax Cover Sheet
- *Electronic version of the letterhead that works in Google Docs (.jpg for top header)

Industry/Entity Type

Property Management

```html
<!DOCTYPE html>
<html lang="en">
<head>
<meta charset="utf-8">
<title>Harrowgate Properties Stationery</title>
<link rel="stylesheet" href="https://fonts.googleapis.com/css2?family=Barlow:wght@400;500;700&display=swap">
<style>
  :root {
    --navy: #2f3d6e;
    --sky: #5ba3cf;
    --paper: #ffffff;
    --ink: #1e1f24;
    --rule: #8a8a8a;
    --backdrop: #e4e5e8;
  }
  * { margin: 0; padding: 0; box-sizing: border-box; }
  html, body { width: 1200px; height: 900px; overflow: hidden; }
  body {
    background: var(--backdrop);
    font-family: "Barlow", sans-serif;
    color: var(--ink);
    position: relative;
  }
  .sheet {
    position: absolute;
    background: var(--paper);
    box-shadow: 0 2px 10px rgba(0,0,0,0.18);
    overflow: hidden;
  }
  .brand-name {
    position: absolute;
    font-family: "Barlow", sans-serif;
    font-weight: 700;
    color: var(--navy);
    line-height: 0.95;
    letter-spacing: -0.01em;
  }
  .header-band {
    position: absolute;
    right: 0;
    background: linear-gradient(to right, rgba(47,61,110,0) 0%, rgba(47,61,110,0.35) 45%, var(--navy) 100%);
  }
  .contact-block {
    position: absolute;
    font-weight: 500;
    line-height: 1.3;
    color: var(--ink);
  }
  .contact-block p + p { margin-top: 0.9em; }
  .accent-block { position: absolute; background: var(--sky); }
  .accent-corner { position: absolute; right: 0; bottom: 0; background: var(--sky); }

  /* Letterhead */
  .letterhead { left: 40px; top: 126px; width: 500px; height: 647px; }
  .letterhead .brand-name { left: 32px; top: 24px; font-size: 30px; }
  .letterhead .header-band { top: 34px; left: 240px; height: 22px; }
  .letterhead .contact-block { left: 340px; top: 464px; font-size: 9.5px; }
  .letterhead .accent-block { left: 340px; top: 584px; width: 62px; height: 28px; }
  .letterhead .accent-corner { width: 46px; height: 20px; }

  /* Envelope */
  .envelope { left: 580px; top: 126px; width: 580px; height: 252px; }
  .envelope .brand-name { left: 60px; top: 26px; font-size: 26px; }
  .envelope .header-band { top: 66px; left: 240px; height: 22px; }
  .envelope .window-line {
    position: absolute; left: 70px; width: 214px; height: 0;
    border-top: 1.5px solid var(--rule);
  }
  .envelope .window-line.first { top: 132px; }
  .envelope .window-line.second { top: 156px; }
  .envelope .contact-block { left: 430px; top: 100px; font-size: 8.5px; }
  .envelope .accent-block { left: 430px; top: 204px; width: 66px; height: 28px; }
  .envelope .accent-corner { width: 48px; height: 16px; }

  /* Business cards */
  .card { top: 420px; width: 280px; height: 160px; }
  .card-back { left: 580px; background: var(--navy); }
  .card-back .brand-name {
    left: 0; right: 0; top: 56px; text-align: center;
    color: var(--paper); font-size: 24px;
  }
  .card-front { left: 880px; }
  .card-front .brand-name { left: 14px; top: 12px; font-size: 12px; }
  .card-front .header-band { top: 30px; left: 120px; height: 10px; }
  .card-front .contact-block { left: 14px; top: 66px; font-size: 6.5px; }
  .card-front .person {
    position: absolute; right: 22px; top: 56px; text-align: right;
  }
  .person-name { font-size: 13px; font-weight: 500; color: var(--sky); letter-spacing: 0.02em; }
  .person-title { font-size: 7.5px; font-weight: 700; color: var(--navy); margin-top: 1px; }
  .person-email { font-size: 7.5px; font-weight: 700; color: var(--navy); margin-top: 12px; }
  .card-front .accent-block { right: 34px; top: 112px; width: 48px; height: 20px; }
  .card-front .accent-corner { width: 32px; height: 12px; }
</style>
</head>
<body>

  <section class="sheet letterhead" aria-label="Letterhead">
    <div class="brand-name">Harrowgate<br>Properties</div>
    <div class="header-band"></div>
    <div class="contact-block">
      <p>Harrowgate Properties Corp.<br>410 Maple Crescent<br>Winnipeg, MB R3C 0A1</p>
      <p>Tel (204) 555-0147<br>Fax (204) 555-0148</p>
      <p>info@harrowgateproperties.ca<br>www.harrowgateproperties.ca</p>
    </div>
    <div class="accent-block"></div>
    <div class="accent-corner"></div>
  </section>

  <section class="sheet envelope" aria-label="Number 10 envelope">
    <div class="brand-name">Harrowgate<br>Properties</div>
    <div class="header-band"></div>
    <div class="window-line first"></div>
    <div class="window-line second"></div>
    <div class="contact-block">
      <p>Harrowgate Properties Corp.<br>410 Maple Crescent<br>Winnipeg, MB R3C 0A1</p>
      <p>Tel (204) 555-0147<br>Fax (204) 555-0148</p>
      <p>info@harrowgateproperties.ca<br>www.harrowgateproperties.ca</p>
    </div>
    <div class="accent-block"></div>
    <div class="accent-corner"></div>
  </section>

  <section class="sheet card card-back" aria-label="Business card back">
    <div class="brand-name">Harrowgate<br>Properties</div>
  </section>

  <section class="sheet card card-front" aria-label="Business card front">
    <div class="brand-name">Harrowgate Properties</div>
    <div class="header-band"></div>
    <div class="contact-block">
      <p>Tel (204) 555-0147<br>Fax (204) 555-0148</p>
      <p>info@harrowgateproperties.ca<br>www.harrowgateproperties.ca</p>
      <p>Harrowgate Properties Corp.<br>410 Maple Crescent<br>Winnipeg, MB R3C 0A1</p>
    </div>
    <div class="person">
      <div class="person-name">Dana Whitlock</div>
      <div class="person-title">President &amp; CEO</div>
      <div class="person-email">dwhitlock@harrowgateproperties.ca</div>
    </div>
    <div class="accent-block"></div>
    <div class="accent-corner"></div>
  </section>

</body>
</html>
```